Business cards for law firm with global theme

I'd like business cards with contact info for two offices. They should include the colors and font of the new logo design, which is a stylized globe with an "F" in it. The feel should be very modern and professional.

```html
<!DOCTYPE html>
<html lang="en">
<head>
<meta charset="utf-8">
<title>Veltraine Law – Business Cards</title>
<link href="https://fonts.googleapis.com/css2?family=Montserrat:wght@400;500;600;700&display=swap" rel="stylesheet">
<style>
  :root {
    --backdrop: #8f8f8f;
    --navy: #043a6b;
    --cyan: #11a9e6;
    --white: #ffffff;
  }
  html, body {
    margin: 0;
    padding: 0;
    width: 1200px;
    height: 1200px;
    overflow: hidden;
    background: var(--backdrop);
  }
  .sheet { position: relative; width: 1200px; height: 1200px; }
  .card { position: absolute; left: 281px; width: 638px; height: 365px; filter: drop-shadow(2px 4px 4px rgba(0,0,0,.35)); }
  .card--front { top: 195px; }
  .card--back { top: 639px; }
  .card text { font-family: "Montserrat", sans-serif; }
  .brand-name { font-size: 27px; font-weight: 600; fill: var(--navy); letter-spacing: .5px; }
  .holder-name { font-size: 27px; font-weight: 700; fill: var(--white); letter-spacing: 1px; }
  .holder-role { font-size: 15px; font-weight: 500; fill: var(--cyan); font-variant: small-caps; letter-spacing: 1px; }
  .contact { font-size: 14px; font-weight: 500; fill: var(--white); letter-spacing: 1px; }
  .address { font-size: 15px; font-weight: 500; fill: var(--white); font-variant: small-caps; letter-spacing: 1px; }
  .icon { fill: var(--cyan); }
</style>
</head>
<body>
<div class="sheet">

  <svg class="card card--front" viewBox="0 0 638 365" xmlns="http://www.w3.org/2000/svg">
    <defs><clipPath id="front-clip"><rect width="638" height="365" rx="22"/></clipPath></defs>
    <g clip-path="url(#front-clip)">
      <rect class="card-face" width="638" height="365" fill="var(--white)"/>
      <path class="wave-accent" d="M0,244 Q230,110 540,138 Q260,122 0,262 Z" fill="var(--cyan)"/>
      <path class="wave-band" d="M0,262 Q260,128 638,162 L638,365 L0,365 Z" fill="var(--navy)"/>
    </g>

    <g class="brand">
      <circle cx="81" cy="77" r="30" fill="var(--navy)"/>
      <text class="brand-name" x="125" y="87">VELTRAINE LAW</text>
    </g>

    <g class="holder" text-anchor="end">
      <text class="holder-name" x="601" y="199">MARCUS HALE</text>
      <text class="holder-role" x="601" y="218">Lawyer</text>
      <rect x="555" y="236" width="46" height="1.5" fill="var(--white)"/>
      <text class="address" x="601" y="266">4127 Linden Court</text>
      <text class="address" x="601" y="285">Hartwell, CT 06492</text>
      <text class="address" x="601" y="311">4127 Linden Court</text>
      <text class="address" x="601" y="330">Hartwell, CT 06492</text>
    </g>

    <g class="contacts">
      <path class="icon" d="M42,256 l3,-1 l2,4 l-2,1.5 q1.5,3 4,4.5 l1.5,-2 l4,2 l-1,3 q-7,0 -11.5,-12 z"/>
      <text class="contact" x="65" y="266">(555) 014-2290</text>
      <rect class="icon" x="44" y="276" width="8" height="13" rx="1.5"/>
      <rect x="46" y="278" width="4" height="7" fill="var(--navy)"/>
      <text class="contact" x="65" y="288">(555) 014-2290</text>
      <rect class="icon" x="42" y="302" width="12" height="8"/>
      <path d="M42,302 l6,4.5 l6,-4.5" stroke="var(--navy)" stroke-width="1.2" fill="none"/>
      <text class="contact" x="65" y="310">MARCUS@VELTRAINELAW.COM</text>
      <circle class="icon" cx="48" cy="326" r="6"/>
      <path d="M44,324 q4,2 8,0 M48,320 v12" stroke="var(--navy)" stroke-width="1" fill="none"/>
      <text class="contact" x="65" y="331">VELTRAINELAW.COM</text>
    </g>
  </svg>

  <svg class="card card--back" viewBox="0 0 638 365" xmlns="http://www.w3.org/2000/svg">
    <defs>
      <linearGradient id="pattern-tone" x1="0" y1="0" x2="1" y2="0">
        <stop offset="0" stop-color="#f2f2f2"/>
        <stop offset=".35" stop-color="#5a5a5a"/>
        <stop offset="1" stop-color="#050505"/>
      </linearGradient>
    </defs>
    <rect class="card-face" width="638" height="365" rx="22" fill="var(--navy)"/>
    <rect class="brand-pattern" x="14" y="15" width="616" height="338" rx="8" fill="url(#pattern-tone)" opacity=".85"
          role="img" aria-label="Repeating grid of brand marks shaded from white to black, with one accent in cyan"/>
  </svg>

</div>
</body>
</html>
```